Clear Cash Blueprint: 8 Simple Steps To Put Your Family Budget On Track

Need a book cover for a book called "Clear Cash Blueprint: 8 Steps To Put Your Family Budget On Track"

The book is 5.5 by 8.5 and has no spine.

I am attaching the current cover but would like to see some other options that you all can come up with.

This book contains 8 specific action items for what people need to do.
Pay down debt. get estate documents in order. Be careful when buying a house, have enough life insurance to pay debt...etc.

Target Market(s)

Target market is parents around 35-55 years old who are concerned about their financial situation.

Industry/Entity Type

Financial Planning

Font styles to use
Serif

Colors

Designer to choose colors to be used in the design.

Requirements
Must have
• Definitely want my picture on the back.
Nice to have
• I'm pretty much open to ideas.

```html
<!DOCTYPE html>
<html lang="en">
<head>
<meta charset="utf-8">
<title>Clear Cash Blueprint – Book Cover</title>
<link rel="stylesheet" href="https://fonts.googleapis.com/css2?family=Cinzel:wght@400;600&family=Source+Sans+3:wght@400;600;700&family=Archivo:wght@700;800&display=swap">
<style>
  :root {
    --title-gold: #d9a91f;
    --title-pale: #e9ddd0;
    --white: #ffffff;
    --ink: #1c1206;
    --bio-fill: rgba(244, 196, 48, 0.82);
    --panel-dark: rgba(22, 14, 4, 0.78);
    --accent-red: #e0221b;
    --accent-yellow: #fde02a;
  }
  * { margin: 0; padding: 0; box-sizing: border-box; }
  html, body { width: 1200px; height: 887px; overflow: hidden; background: #fff; }
  .cover {
    position: relative;
    width: 1200px;
    height: 887px;
    overflow: hidden;
    font-family: "Source Sans 3", sans-serif;
  }
  .coin-backdrop {
    position: absolute; inset: 0;
    background:
      radial-gradient(ellipse 55% 40% at 70% 30%, rgba(255,220,110,0.95), rgba(255,200,70,0) 70%),
      radial-gradient(ellipse 60% 45% at 80% 65%, rgba(230,160,40,0.9), rgba(200,120,20,0) 75%),
      radial-gradient(ellipse 40% 35% at 30% 85%, rgba(170,110,30,0.7), rgba(120,70,10,0) 75%),
      linear-gradient(135deg, #4a2606 0%, #8a4e0e 30%, #c98a1a 55%, #9a5a10 80%, #5a3008 100%);
  }

  /* Back cover */
  .back-title {
    position: absolute; left: 38px; top: 38px;
    font-family: "Cinzel", serif; font-weight: 400; line-height: 0.98;
    color: var(--title-pale);
  }
  .back-title span { display: block; }
  .back-title .t1 { font-size: 72px; letter-spacing: 1px; }
  .back-title .t2 { font-size: 104px; color: var(--title-gold); letter-spacing: 1px; }
  .back-title .t3 { font-size: 72px; }

  .author-bio {
    position: absolute; left: 0; top: 297px;
    width: 577px; height: 238px;
    background: var(--bio-fill);
    border-radius: 0 22px 22px 0;
    border: 2px solid rgba(255,220,120,0.6);
    border-left: none;
  }
  .author-photo {
    position: absolute; left: 20px; top: 4px;
    width: 229px; height: 229px;
    border-radius: 18px;
    background: linear-gradient(160deg, #8e8a82 0%, #5d5c58 45%, #a7a49c 100%);
  }
  .author-text {
    position: absolute; left: 268px; top: 22px; width: 283px;
    font-size: 18.5px; line-height: 23.6px; color: var(--ink);
    text-align: justify;
  }
  .author-text strong { font-size: 22px; font-weight: 600; }

  .praise-panel {
    position: absolute; left: -4px; top: 550px;
    width: 581px; height: 345px;
    background: var(--panel-dark);
    border: 2px solid var(--accent-red);
    border-radius: 0 26px 0 0;
    padding: 18px 28px 0 46px;
    color: var(--white);
  }
  .praise-heading {
    font-size: 21px; color: var(--accent-yellow); font-weight: 400;
    letter-spacing: 0.3px; margin-bottom: 6px;
  }
  .praise-heading b { font-weight: 700; }
  .praise-quote { font-size: 15px; line-height: 20px; text-align: justify; }
  .praise-source { font-size: 15px; font-weight: 700; line-height: 20px; }
  .availability { margin-top: 30px; font-size: 16px; line-height: 21.5px; }
  .availability strong { font-size: 17.5px; }
  .price { margin-top: 12px; font-size: 18px; font-weight: 700; }

  /* Front cover */
  .author-name {
    position: absolute; left: 676px; top: 48px;
    font-family: "Archivo", sans-serif; font-weight: 800;
    font-size: 30px; color: var(--white); letter-spacing: 0.5px;
  }
  .front-title {
    position: absolute; right: 62px; top: 108px;
    font-family: "Cinzel", serif; font-weight: 600;
    color: var(--white); text-align: right; line-height: 0.95;
  }
  .front-title span { display: block; }
  .front-title .t1 { font-size: 78px; }
  .front-title .t2 { font-size: 112px; }
  .front-title .t3 { font-size: 74px; }

  .steps-banner {
    position: absolute; left: 646px; top: 703px;
    width: 580px; height: 140px;
    background: rgba(20, 10, 2, 0.85);
    border: 5px solid var(--accent-red);
    border-right: none;
    border-radius: 70px 0 0 70px;
  }
  .steps-number {
    position: absolute; left: 56px; top: 6px;
    font-family: "Archivo", sans-serif; font-weight: 800;
    font-size: 110px; line-height: 120px; color: var(--accent-yellow);
  }
  .steps-text {
    position: absolute; left: 140px; top: 32px;
    font-family: "Archivo", sans-serif; font-weight: 700;
    font-size: 27px; line-height: 35px; color: var(--white); letter-spacing: 0.5px;
  }
</style>
</head>
<body>
<main class="cover">
  <div class="coin-backdrop" role="img" aria-label="Close-up photograph of a pile of glowing gold coins"></div>

  <section class="back-cover">
    <h2 class="back-title"><span class="t1">CLEAR</span><span class="t2">CASH</span><span class="t3">BLUEPRINT</span></h2>

    <div class="author-bio">
      <div class="author-photo" role="img" aria-label="Portrait photograph of the author in a grey suit"></div>
      <p class="author-text"><strong>Mark Hollins</strong> has provided financial advice since 1998 in areas of investment management, Social Security, tax, retirement planning and wealth transfer strategies. Mark believes that complexity is the enemy of successful financial planning.</p>
    </div>

    <div class="praise-panel">
      <h3 class="praise-heading">PRAISE FOR <b>CLEAR CASH BLUEPRINT</b></h3>
      <p class="praise-quote">“Beginning with prudent advice on debt and debt management and concluding with reasons for estate planning at an early age, Hollins provides simple yet applicable strategies for anyone to use confidently – and secure a more stable financial future. About as real and raw as it comes.”</p>
      <p class="praise-source">- Dana Whitfield, Ashford, Oregon</p>
      <p class="availability"><strong>Clear Cash Blueprint</strong> is available at<br>www.northfieldplanning.com, or by emailing<br>Mark@northfieldplanning.com.</p>
      <p class="price">$18.95</p>
    </div>
  </section>

  <section class="front-cover">
    <p class="author-name">MARK HOLLINS, MBA, MS</p>
    <h1 class="front-title"><span class="t1">CLEAR</span><span class="t2">CASH</span><span class="t3">BLUEPRINT</span></h1>
    <div class="steps-banner">
      <span class="steps-number">8</span>
      <p class="steps-text">STEPS TO PUT YOUR<br>FAMILY BUDGET ON TRACK</p>
    </div>
  </section>
</main>
</body>
</html>
```